Email Signature Block Design for Law Firm

I would like you to create a similar signature block for my law firm . I saw the email signature block attached as image002.png and wanted a similar design for my law firm. I want to be able to swap the portraits for each of my staff from the final design. Our law firm colors are black, gold, white, red.

Industry/Entity Type

Law

Requirements
Nice to have
• i like the red circle in around the photo in the 8 copper bench design. The 9 Copper Bench desgn is what inspired me to have a signature block design for my firm.

```html
<!DOCTYPE html>
<html lang="en">
<head>
<meta charset="utf-8">
<title>Harlow Firm Email Signature</title>
<link rel="stylesheet" href="https://fonts.googleapis.com/css2?family=Cinzel:wght@500;600&family=Lato:wght@400;700&display=swap">
<style>
  :root {
    --ink: #000000;
    --gold: #d99a2b;
    --gold-soft: #c98f2a;
    --paper: #ffffff;
    --slate: #5a5a5a;
    --badge: #b9b9b9;
    --photo-light: #f2f2f2;
    --photo-dark: #2a2d35;
  }
  * { box-sizing: border-box; margin: 0; padding: 0; }
  html, body { width: 1200px; height: 400px; overflow: hidden; background: var(--paper); }
  .signature {
    position: relative;
    width: 1200px;
    height: 400px;
    background: var(--paper);
    font-family: "Lato", sans-serif;
    overflow: hidden;
  }
  .signature__band {
    position: absolute;
    left: 0; top: 0;
    width: 1200px; height: 305px;
    background: var(--ink);
  }
  .brand {
    position: absolute;
    left: 44px; top: 48px;
    display: flex;
    align-items: center;
    gap: 14px;
  }
  .brand__mark {
    width: 54px; height: 54px;
    background: var(--gold);
  }
  .brand__text { display: flex; flex-direction: column; }
  .brand__name {
    font-family: "Cinzel", serif;
    font-weight: 600;
    font-size: 20px;
    color: var(--paper);
    letter-spacing: 0.5px;
    white-space: nowrap;
  }
  .brand__name small { font-size: 13px; }
  .brand__tagline {
    display: flex;
    align-items: center;
    gap: 6px;
    margin-top: 4px;
    font-family: "Cinzel", serif;
    font-size: 10px;
    letter-spacing: 3.5px;
    color: var(--paper);
    white-space: nowrap;
  }
  .brand__tagline::before,
  .brand__tagline::after {
    content: "";
    display: block;
    width: 20px; height: 1px;
    background: var(--paper);
  }
  .attorney {
    position: absolute;
    left: 39px; top: 168px;
  }
  .attorney__name {
    font-family: "Cinzel", serif;
    font-weight: 500;
    font-size: 32px;
    line-height: 1;
    color: var(--gold);
    letter-spacing: 1px;
    white-space: nowrap;
  }
  .attorney__name small { font-size: 24px; }
  .attorney__role {
    margin-top: 12px;
    font-family: "Cinzel", serif;
    font-weight: 600;
    font-size: 15px;
    color: var(--paper);
    letter-spacing: 0.8px;
  }
  .portrait {
    position: absolute;
    left: 430px; top: 24px;
    width: 340px; height: 340px;
    border-radius: 50%;
    background: var(--gold);
    padding: 19px;
  }
  .portrait__photo {
    width: 100%; height: 100%;
    border-radius: 50%;
    background: linear-gradient(180deg, var(--photo-light) 0%, var(--photo-light) 48%, var(--photo-dark) 72%, var(--photo-dark) 100%);
  }
  .contact {
    position: absolute;
    left: 814px; top: 112px;
    list-style: none;
  }
  .contact__item {
    display: flex;
    align-items: center;
    gap: 12px;
    height: 31px;
    font-size: 21px;
    color: var(--paper);
    white-space: nowrap;
  }
  .contact__icon {
    width: 22px; height: 22px;
    border-radius: 50%;
    background: var(--gold);
    display: flex;
    align-items: center;
    justify-content: center;
    flex: none;
  }
  .contact__icon svg { width: 13px; height: 13px; }
  .address {
    position: absolute;
    left: 41px; top: 324px;
    font-size: 19px;
    line-height: 30px;
    color: var(--slate);
    font-style: normal;
  }
  .recognition {
    position: absolute;
    left: 796px; top: 340px;
    display: flex;
    align-items: center;
    gap: 22px;
  }
  .recognition__badge { background: var(--badge); height: 22px; }
  .recognition__badge--wide { width: 102px; }
  .recognition__badge--mid { width: 86px; }
  .recognition__badge--trend { width: 70px; height: 30px; }
  .recognition__badge--seal { width: 40px; height: 40px; border-radius: 50%; }
</style>
</head>
<body>
  <main class="signature">
    <div class="signature__band"></div>

    <div class="brand">
      <div class="brand__mark"></div>
      <div class="brand__text">
        <span class="brand__name">The Harlow Firm, <small>PLLC</small></span>
        <span class="brand__tagline">Attorneys At Law</span>
      </div>
    </div>

    <div class="attorney">
      <h1 class="attorney__name">Marcus Harlow, <small>ESQ</small></h1>
      <p class="attorney__role">Personal Injury Lawyers</p>
    </div>

    <div class="portrait">
      <div class="portrait__photo" role="img" aria-label="Staff portrait: attorney in dark suit, white shirt and blue striped tie on a white background"></div>
    </div>

    <ul class="contact">
      <li class="contact__item">
        <span class="contact__icon">
          <svg viewBox="0 0 24 24" aria-hidden="true"><path fill="#000" d="M6.6 10.8a15.1 15.1 0 0 0 6.6 6.6l2.2-2.2c.3-.3.7-.4 1-.2 1.1.4 2.3.6 3.6.6.6 0 1 .4 1 1V20c0 .6-.4 1-1 1A17 17 0 0 1 3 4c0-.6.4-1 1-1h3.5c.6 0 1 .4 1 1 0 1.3.2 2.5.6 3.6.1.3 0 .7-.2 1z"/></svg>
        </span>
        205-555-0148
      </li>
      <li class="contact__item">
        <span class="contact__icon">
          <svg viewBox="0 0 24 24" aria-hidden="true"><path fill="#000" d="M3 5h18v14H3z"/><path fill="none" stroke="#d99a2b" stroke-width="2" d="M3 6l9 7 9-7"/></svg>
        </span>
        contact@harlow-firm.com
      </li>
      <li class="contact__item">
        <span class="contact__icon"></span>
        harlowfirmlaw
      </li>
    </ul>

    <address class="address">
      412 N Cedar St Suite 300<br>
      Riverton, FL 32590
    </address>

    <div class="recognition" aria-label="Recognitions">
      <div class="recognition__badge recognition__badge--wide"></div>
      <div class="recognition__badge recognition__badge--mid"></div>
      <div class="recognition__badge recognition__badge--trend"></div>
      <div class="recognition__badge recognition__badge--seal"></div>
    </div>
  </main>
</body>
</html>
```